Magician | Speaker looks for an innovative business card design

I'm a magician and public speaker offering artistic and modern magical experiences.
I'm based in Brussels (Belgium.) I love magic performed up-close, creating a space of intimacy, even when I'm on stage.
The final design should communicate professionalism, elegance, artistry, and a friendly kind personality

I would like to see designs based either on my photos and/or the way I sign my name Remy Vok (see attached files for more info.)
Additional photos and more info about what I offer can be seen at www.remy-vok.net

My current business card design is also attached. I like the fact that the reverse of my current design includes quotes from master magicians about magic, changing the way my participants see the art of magic.

Note: I would like a double-sided card design. However, I need white space on the reverse to be able to write things on for my performances.

Details to include on the card:
Artist name: Remy Vok
Offer: magician + (public) speaker or magic + (public) speaking (the + sign can be replaced by another character, like a bullet or a pipe)
Phone: +32 471 265 903
Email: book@remy-vok.net
(optional) Website: www.remy-vok.net or remy-vok.net

Target Market(s)

Corporate, organisations, companies as well as individuals

Industry/Entity Type

Artists

Colors

Designer to choose colors to be used in the design.

Requirements
Nice to have
• A side with a mirror could be nice

```html
<!DOCTYPE html>
<html lang="en">
<head>
<meta charset="utf-8">
<title>Remy Vok – Business Card</title>
<link href="https://fonts.googleapis.com/css2?family=Open+Sans:wght@300;400&display=swap" rel="stylesheet">
<style>
  :root {
    --backdrop: #738386;
    --paper: #ecf2f1;
    --ink: #111111;
    --white: #ffffff;
    --violet: #8a45fb;
    --lime: #63d12f;
    --royal: #285cdc;
    --magenta: #b52c80;
    --jade: #20a36f;
    --sky: #add8ee;
    --label-blue: #3b86ee;
  }
  html, body {
    margin: 0;
    padding: 0;
    overflow: hidden;
  }
  .canvas {
    position: relative;
    width: 1200px;
    height: 1200px;
    background: var(--backdrop);
    font-family: "Open Sans", Arial, sans-serif;
    overflow: hidden;
  }
  .card {
    position: absolute;
    top: 171px;
    width: 540px;
    height: 899px;
    background: var(--paper);
  }
  .card--front { left: 29px; }
  .card--back { left: 631px; }

  .name-mark {
    position: absolute;
    color: var(--ink);
    font-weight: 400;
    white-space: nowrap;
    letter-spacing: 1px;
  }
  .card--front .name-mark {
    left: 0;
    width: 540px;
    top: 95px;
    height: 100px;
    line-height: 100px;
    text-align: center;
    font-size: 74px;
  }

  .band {
    position: absolute;
    left: 1px;
    width: 539px;
    height: 116px;
    display: flex;
    align-items: center;
    justify-content: center;
    text-align: center;
    color: var(--white);
  }
  .band--phone { top: 239px; background: var(--violet); font-size: 32px; letter-spacing: 1px; }
  .band--email { top: 363px; background: var(--lime); font-size: 33px; letter-spacing: 0.5px; }
  .band--web { top: 487px; background: var(--royal); font-size: 33px; letter-spacing: 1px; }
  .band--offer { top: 611px; background: var(--magenta); font-size: 25px; line-height: 32px; letter-spacing: 0.5px; }
  .band--quote { top: 735px; background: var(--jade); font-size: 24px; font-weight: 300; line-height: 31px; }

  .accent-block {
    position: absolute;
    left: 252px;
    top: 32px;
    width: 250px;
    height: 444px;
    background: var(--sky);
  }
  .photo {
    position: absolute;
    display: block;
  }
  .photo--portrait { left: 59px; top: 60px; width: 258px; height: 387px; }
  .photo--cards-table { left: 60px; top: 454px; width: 206px; height: 211px; }
  .photo--coin { left: 274px; top: 454px; width: 206px; height: 211px; }
  .photo--card-flourish { left: 60px; top: 670px; width: 206px; height: 211px; }
  .photo--reveal { left: 274px; top: 670px; width: 206px; height: 211px; }

  .name-box {
    position: absolute;
    left: 291px;
    top: 332px;
    width: 172px;
    height: 82px;
    background: var(--paper);
  }
  .name-box .name-mark {
    left: 0;
    width: 172px;
    top: 22px;
    height: 44px;
    line-height: 44px;
    text-align: center;
    font-size: 30px;
  }
  .role-label {
    position: absolute;
    left: 224px;
    top: 414px;
    width: 256px;
    height: 34px;
    background: var(--label-blue);
    color: var(--white);
    font-size: 14.5px;
    display: flex;
    align-items: center;
    justify-content: center;
    white-space: nowrap;
  }
</style>
</head>
<body>
<div class="canvas">

  <section class="card card--front">
    <div class="name-mark">Remy Vok</div>
    <div class="band band--phone">Phone: +32 471 265 903</div>
    <div class="band band--email">book@remy-vok.net</div>
    <div class="band band--web">www.remy-vok.net</div>
    <div class="band band--offer">magician + (public) speaker,<br>magic + (public) speaking</div>
    <div class="band band--quote">“The world is full of magic things,<br>patiently waiting for our senses to<br>grow sharper.”</div>
  </section>

  <section class="card card--back">
    <div class="accent-block"></div>

    <svg class="photo photo--portrait" role="img" aria-label="Portrait photo of the magician seated in a dark jacket against a brick wall" viewBox="0 0 258 387" preserveAspectRatio="none">
      <defs>
        <radialGradient id="portraitTone" cx="0.55" cy="0.4" r="0.7">
          <stop offset="0" stop-color="#3a2a24"/>
          <stop offset="1" stop-color="#0b0908"/>
        </radialGradient>
      </defs>
      <rect width="258" height="387" fill="url(#portraitTone)"/>
    </svg>

    <div class="name-box"><div class="name-mark">Remy Vok</div></div>
    <div class="role-label">MAGICIAN AND PUBLIC SPEAKER</div>

    <svg class="photo photo--cards-table" role="img" aria-label="Photo of playing cards being spread on a wooden table for a guest" viewBox="0 0 206 211" preserveAspectRatio="none">
      <defs>
        <linearGradient id="tableTone" x1="0" y1="0" x2="1" y2="1">
          <stop offset="0" stop-color="#8a6a4c"/>
          <stop offset="0.6" stop-color="#4a2a1a"/>
          <stop offset="1" stop-color="#141210"/>
        </linearGradient>
      </defs>
      <rect width="206" height="211" fill="url(#tableTone)"/>
    </svg>

    <svg class="photo photo--coin" role="img" aria-label="Close-up photo of a hand holding coins between the fingers" viewBox="0 0 206 211" preserveAspectRatio="none">
      <defs>
        <linearGradient id="coinTone" x1="0" y1="0" x2="1" y2="1">
          <stop offset="0" stop-color="#7c2b47"/>
          <stop offset="0.5" stop-color="#3a1e22"/>
          <stop offset="1" stop-color="#b08070"/>
        </linearGradient>
      </defs>
      <rect width="206" height="211" fill="url(#coinTone)"/>
    </svg>

    <svg class="photo photo--card-flourish" role="img" aria-label="Photo of cards falling from one hand into the other" viewBox="0 0 206 211" preserveAspectRatio="none">
      <defs>
        <linearGradient id="flourishTone" x1="0" y1="0" x2="1" y2="1">
          <stop offset="0" stop-color="#2a2320"/>
          <stop offset="0.5" stop-color="#12151c"/>
          <stop offset="1" stop-color="#1c2232"/>
        </linearGradient>
      </defs>
      <rect width="206" height="211" fill="url(#flourishTone)"/>
    </svg>

    <svg class="photo photo--reveal" role="img" aria-label="Photo of a card reveal across a round wooden table" viewBox="0 0 206 211" preserveAspectRatio="none">
      <defs>
        <linearGradient id="revealTone" x1="0" y1="0" x2="0" y2="1">
          <stop offset="0" stop-color="#0e0d0c"/>
          <stop offset="0.6" stop-color="#4a2618"/>
          <stop offset="1" stop-color="#1a100c"/>
        </linearGradient>
      </defs>
      <rect width="206" height="211" fill="url(#revealTone)"/>
    </svg>
  </section>

</div>
</body>
</html>
```